Lantern Hearthworks Business Cards

Looking to create simple business cards that highlight our unique three sided triangle fire pit design with the colors and font of our logo, listed below.

Colors

Designer to choose colors to be used in the design.

Requirements
Must have
• Looking for something simple that includes a picture of our fire pit with name, website (lanternhearthworks.com), phone number and email. Want to keep the color mostly orange and black.
• Font is gotham(medium) and orange color code is #ee6e22

```html
<!DOCTYPE html>
<html lang="en">
<head>
<meta charset="utf-8">
<title>Lantern Hearthworks Business Cards</title>
<link href="https://fonts.googleapis.com/css2?family=Montserrat:wght@400;500;600&display=swap" rel="stylesheet">
<style>
  :root {
    --backdrop: #161616;
    --card: #232323;
    --card-edge: #2c2c2c;
    --ink-silver: #b8b8b8;
    --ink-bright: #d9d9d9;
    --ink-muted: #9a9a9a;
    --rule: #7a7a7a;
    --ember: #ee6e22;
  }
  * { margin: 0; padding: 0; box-sizing: border-box; }
  html, body {
    width: 1200px; height: 900px; overflow: hidden;
    background: var(--backdrop);
    font-family: "Montserrat", sans-serif;
  }
  .sheet { position: relative; width: 1200px; height: 900px; }
  .card {
    position: absolute;
    background: linear-gradient(135deg, var(--card) 0%, #1f1f1f 60%, var(--card-edge) 100%);
    box-shadow: 0 18px 40px rgba(0,0,0,0.55);
  }
  .card--front { left: 300px; top: 60px; width: 600px; height: 343px; }
  .card--back { left: 260px; top: 450px; width: 680px; height: 389px; }

  .brand-mark {
    position: absolute;
    background: var(--ember);
  }
  .card--front .brand-mark { left: 130px; top: 137px; width: 70px; height: 70px; }
  .card--back .brand-mark { left: 52px; top: 165px; width: 48px; height: 48px; }

  .divider { position: absolute; width: 1px; background: var(--rule); }
  .card--front .divider { left: 225px; top: 112px; height: 120px; }
  .card--back .divider--brand { left: 120px; top: 145px; height: 90px; }
  .card--back .divider--contact { left: 372px; top: 125px; height: 130px; }

  .wordmark {
    position: absolute;
    color: var(--ink-silver);
    font-weight: 500;
    text-transform: uppercase;
    letter-spacing: 0.16em;
    line-height: 1.1;
  }
  .card--front .wordmark { left: 248px; top: 138px; font-size: 30px; }
  .card--back .wordmark { left: 136px; top: 163px; font-size: 21px; }

  .contact { position: absolute; left: 394px; top: 128px; color: var(--ink-silver); }
  .contact__name { font-size: 23px; font-weight: 600; color: var(--ink-bright); letter-spacing: 0.02em; }
  .contact__role { font-size: 14px; font-weight: 400; color: var(--ink-muted); margin-top: 2px; margin-bottom: 14px; }
  .contact__line { display: flex; align-items: center; gap: 8px; font-size: 15px; margin-top: 5px; }
  .contact__line svg { width: 12px; height: 12px; flex: none; }
</style>
</head>
<body>
<main class="sheet">
  <section class="card card--front">
    <div class="brand-mark" role="img" aria-label="Fire pit brand mark placeholder"></div>
    <div class="divider"></div>
    <div class="wordmark">Lantern<br>Hearthworks</div>
  </section>

  <section class="card card--back">
    <div class="brand-mark" role="img" aria-label="Fire pit brand mark placeholder"></div>
    <div class="divider divider--brand"></div>
    <div class="wordmark">Lantern<br>Hearthworks</div>
    <div class="divider divider--contact"></div>
    <div class="contact">
      <div class="contact__name">MARCUS DELVANE</div>
      <div class="contact__role">CO-Founder</div>
      <div class="contact__line">
        <svg viewBox="0 0 12 12" aria-hidden="true"><path d="M2.5 1h2l1 2.5-1.3 1a6 6 0 0 0 3.3 3.3l1-1.3L11 7.5v2A1.5 1.5 0 0 1 9.5 11 8.5 8.5 0 0 1 1 2.5 1.5 1.5 0 0 1 2.5 1z" fill="#b8b8b8"/></svg>
        <span>503-555-0148</span>
      </div>
      <div class="contact__line">
        <svg viewBox="0 0 12 12" aria-hidden="true"><rect x="1" y="2.5" width="10" height="7" fill="none" stroke="#b8b8b8" stroke-width="1.2"/><path d="M1 2.5l5 4 5-4" fill="none" stroke="#b8b8b8" stroke-width="1.2"/></svg>
        <span>hello@lanternhearthworks.com</span>
      </div>
      <div class="contact__line">
        <svg viewBox="0 0 12 12" aria-hidden="true"><circle cx="6" cy="6" r="5" fill="none" stroke="#b8b8b8" stroke-width="1.1"/><ellipse cx="6" cy="6" rx="2.2" ry="5" fill="none" stroke="#b8b8b8" stroke-width="1"/><path d="M1 6h10" stroke="#b8b8b8" stroke-width="1"/></svg>
        <span>www.lanternhearthworks.com</span>
      </div>
    </div>
  </section>
</main>
</body>
</html>
```